Letterhead Design Project

Please see attached logo as well as information below which could be relevant to design. Let me know if you have any questions.

Derek J. Holloman
Estate Planning and Insurance Specialist
Dholloman@brenwickfinancial.com
P: 516-471-2958 F: 516-471-3085
www.brenwickfinancial.com
4300 Maple Ridge Road, Suite 305E
Syosset, New York 11804

```html
<!DOCTYPE html>
<html lang="en">
<head>
<meta charset="utf-8">
<title>Brenwick Financial Group Letterhead</title>
<link href="https://fonts.googleapis.com/css2?family=Libre+Baskerville:wght@400;700&display=swap" rel="stylesheet">
<style>
  :root {
    --backdrop: #222222;
    --paper: #fefefe;
    --ink-dark: #0f0f12;
    --gold: #d8c79b;
    --cream: #ece4cf;
    --muted: #c9c4b6;
    --band-grey: #8a8589;
    --block-grey: #7c7c7c;
    --haze: rgba(196, 194, 212, 0.55);
    --haze-soft: rgba(196, 194, 212, 0.18);
  }
  * { margin: 0; padding: 0; box-sizing: border-box; }
  html, body { width: 857px; height: 1200px; overflow: hidden; }
  body {
    background: var(--backdrop);
    position: relative;
    font-family: "Libre Baskerville", Georgia, serif;
  }
  .letterhead {
    position: absolute;
    left: 137px; top: 168px;
    width: 585px; height: 828px;
    background: var(--paper);
  }
  .contact-band {
    position: absolute;
    left: 13px; top: 13px;
    width: 440px; height: 109px;
    background: var(--ink-dark);
    padding: 11px 14px;
    color: var(--muted);
    font-size: 8.5px;
    line-height: 12px;
    white-space: nowrap;
  }
  .contact-band .name {
    color: var(--gold);
    font-weight: 700;
    font-size: 12.5px;
    line-height: 16px;
  }
  .contact-band .role {
    font-size: 6.5px;
    line-height: 9px;
    margin-bottom: 11px;
  }
  .contact-band .web {
    color: var(--gold);
    font-weight: 700;
    font-size: 10.5px;
    line-height: 13px;
  }
  .contact-band .label { color: var(--gold); font-weight: 700; }
  .brand-block {
    position: absolute;
    left: 461px; top: 13px;
    width: 111px; height: 109px;
    background: var(--ink-dark);
    display: flex; align-items: center; justify-content: center;
    color: var(--gold);
    font-size: 14px;
  }
  .backdrop-wash {
    position: absolute;
    left: 150px; top: 140px;
    width: 425px; height: 570px;
    background:
      radial-gradient(ellipse at 55% 50%, var(--haze) 0%, var(--haze-soft) 55%, rgba(255,255,255,0) 75%);
  }
  .footer-band {
    position: absolute;
    left: 13px; top: 732px;
    width: 439px; height: 82px;
    background: var(--band-grey);
    display: flex; align-items: center;
    padding-left: 24px;
    gap: 12px;
  }
  .footer-band .mark {
    flex: none;
    width: 60px; height: 62px;
    border: 2px solid var(--cream);
  }
  .footer-band .wordmark {
    color: var(--cream);
    font-size: 16px;
    letter-spacing: 0.4px;
    text-transform: uppercase;
    white-space: nowrap;
  }
  .footer-block {
    position: absolute;
    left: 461px; top: 732px;
    width: 111px; height: 82px;
    background: var(--block-grey);
  }
</style>
</head>
<body>
  <div class="letterhead">
    <header class="contact-band">
      <div class="name">Derek J. Holloman</div>
      <div class="role">Estate Planning and Insurance Specialist</div>
      <div class="web">www.brenwickfinancial.com</div>
      <div>Dholloman@brenwickfinancial.com</div>
      <div><span class="label">Phone:</span> 516-471-2958 <span class="label">Fax:</span> 516-471-3085</div>
      <div>4300 Maple Ridge Road, Suite 305E, Syosset, New York 11804</div>
    </header>
    <div class="brand-block">Brenwick</div>

    <div class="backdrop-wash" role="img" aria-label="Soft lavender background decoration of overlapping translucent squares"></div>

    <footer class="footer-band">
      <div class="mark"></div>
      <div class="wordmark">Brenwick Financial Group</div>
    </footer>
    <div class="footer-block"></div>
  </div>
</body>
</html>
```